update company powerpoint deck - inject more power/personality into the deck

We would like a designer to provide us with a powerpoint template based on our brand guidelines. Current brand guidelines, colours and existing deck provided.
Current deck lacks punch. We really like our black and white elements - but need options for graphs, tables and charts. We potentially need more supplementary colours to what is currently in our brand guidelines.

Target Market(s)

listed companies - B2B. We are a management consulting company.

Industry/Entity Type

Consulting

Font styles to use
Serif
Sans Serif

Requirements
Must have
• Slides that are common for consulting companies.
The ability to use the deck as a report - not just a presentation format

```html
<!DOCTYPE html>
<html lang="en">
<head>
<meta charset="utf-8">
<title>Calder Voss – Presentation Template Overview</title>
<link href="https://fonts.googleapis.com/css2?family=Lato:wght@300;400;700&display=swap" rel="stylesheet">
<style>
:root{
  --teal:#6db5a6;
  --teal-dark:#4e998a;
  --teal-soft:#8cc6ba;
  --navy:#1c2d5a;
  --blue:#3f63a8;
  --red:#b2202f;
  --ink:#222;
  --grey:#666;
  --mute:#9a9a9a;
  --line:#d6d6d6;
  --dots:#f0f2f2;
  --charcoal:#5c5c5c;
}
*{box-sizing:border-box}
html,body{margin:0;width:900px;height:1200px;overflow:hidden;background:#fff}
body{font-family:'Lato',sans-serif;color:var(--ink)}
.deck{position:relative;width:900px;height:1200px}
.slide{position:absolute;width:247px;height:140px;background:#fff;box-shadow:0 2px 7px rgba(0,0,0,.2);overflow:hidden}
.slide > *{position:absolute;margin:0}
.c1{left:43px}.c2{left:320px}.c3{left:599px}
.r1{top:54px}.r2{top:210px}.r3{top:366px}.r4{top:522px}.r5{top:678px}.r6{top:834px}.r7{top:990px}

.dot-field{background:var(--dots)}
.heading{left:26px;top:13px;font-size:8px;font-weight:400;text-transform:uppercase;letter-spacing:.1px;white-space:nowrap}
.heading.center{left:0;width:100%;text-align:center}
.kicker{left:26px;top:23px;font-size:2.8px;color:var(--teal);line-height:1.3}
.kicker.center{left:20px;width:207px;text-align:center}
.foot{left:9px;bottom:5px;font-size:2.2px;color:var(--mute)}
.page{right:9px;bottom:5px;font-size:2.2px;color:var(--mute);letter-spacing:.6px}
.body-copy{font-size:2.6px;line-height:1.55;color:var(--grey);text-align:justify}

.brand{font-size:6px;letter-spacing:4px;text-align:center;line-height:1.7;left:0;width:100%}
.cover-title{left:0;width:100%;text-align:center;font-size:7.5px;letter-spacing:1.2px}
.cover-sub{left:0;width:100%;text-align:center;font-size:2.6px}

.agenda{list-style:none;padding:0}
.agenda li{position:relative;height:12.2px;padding-left:16px}
.agenda .num{position:absolute;left:0;top:0;font-size:6.5px;font-weight:300;color:var(--teal)}
.agenda .item{display:block;font-size:3.6px;text-transform:uppercase;padding-top:1px}
.agenda .desc{display:block;font-size:2.5px;color:var(--grey)}
.agenda.plain .item{text-transform:none}

.photo{background:linear-gradient(160deg,#4d5a6c,#1d2634 70%,#3a3324)}
.portrait{border-radius:50%;background:radial-gradient(circle at 50% 40%,#c9ccd1,#7d848e);border:2px solid #fff}
.welcome{font-size:7px;color:#555;line-height:1.3;text-transform:uppercase}
.signed{font-size:3.2px;color:#444;text-align:right;line-height:1.4}
.signed small{display:block;font-size:2.3px;color:var(--grey)}

.svc{width:15px;height:15px;background:var(--teal)}
.svc-label{font-size:2.2px;color:var(--teal);line-height:1.25;text-transform:uppercase;width:36px}

.tile-icon{background:var(--teal)}
.bullets{font-size:3.9px;line-height:1.32;color:#222;padding-left:8px}
.bullets li{padding-left:1px}

.big-num{font-size:17px;font-weight:300;color:var(--teal);line-height:1}
.num-label{font-size:2.6px;text-transform:uppercase;color:#333}

.col-num{font-size:15px;font-weight:300;color:var(--teal);line-height:1}
.col-head{font-size:2.8px;text-transform:uppercase;color:#333}
.col-copy{font-size:2.5px;line-height:1.4;color:var(--grey);width:40px}

.tile{color:#fff;padding:4px 5px}
.tile b{display:block;font-size:3.6px;line-height:1.25;font-weight:700}
.tile span{display:block;font-size:2.3px;line-height:1.4;margin-top:3px;opacity:.9}

svg text{font-family:'Lato',sans-serif}
</style>
</head>
<body>
<main class="deck">

<!-- Row 1 -->
<section class="slide c1 r1" style="background:var(--teal)">
  <div role="img" aria-label="World map rendered in fine dots" style="left:10px;top:6px;width:227px;height:68px;background:linear-gradient(180deg,rgba(255,255,255,.12),rgba(255,255,255,0))"></div>
  <p class="brand" style="top:12px;color:#fff">CALDER<br>VOSS</p>
  <h1 class="cover-title" style="top:99px;color:#fff;font-weight:400">YOUR TITLE PRESENTATION GOES HERE</h1>
  <p class="cover-sub" style="top:123px;color:#fff">YOUR SUB TITLE PRESENTATION GOES HERE</p>
</section>

<section class="slide c2 r1">
  <div role="img" aria-label="World map rendered in fine dots on navy" style="left:6px;top:5px;width:236px;height:76px;background:linear-gradient(180deg,#22356a,var(--navy))"></div>
  <p class="brand" style="top:12px;color:#fff">CALDER<br>VOSS</p>
  <h1 class="cover-title" style="top:99px;color:var(--navy);font-weight:400">YOUR TITLE PRESENTATION GOES HERE</h1>
  <p class="cover-sub" style="top:123px;color:var(--navy)">YOUR SUB TITLE PRESENTATION GOES HERE</p>
</section>

<section class="slide c3 r1">
  <div class="dot-field" style="right:0;top:0;width:75px;height:22px"></div>
  <div class="dot-field" style="left:0;top:55px;width:70px;height:85px"></div>
  <h2 class="heading" style="top:11px;text-transform:none;font-size:8.5px">Agenda</h2>
  <p class="kicker" style="top:22px">May 27, 2021</p>
  <ol class="agenda" style="left:79px;top:28px;width:160px">
    <li><span class="num">01</span><span class="item">Opportunity</span><span class="desc">Investment Highlights</span></li>
    <li><span class="num">02</span><span class="item">Property Overview</span><span class="desc">Property Description, Market Overview</span></li>
    <li><span class="num">03</span><span class="item">Market Overview</span><span class="desc">Submarket Overview &amp; Comparables</span></li>
    <li><span class="num">04</span><span class="item">Business Plan</span><span class="desc">Renovations, Timeline, Case Study</span></li>
    <li><span class="num">05</span><span class="item">Investment Structure</span><span class="desc">Summary of Terms, Sample Investment</span></li>
    <li><span class="num">06</span><span class="item">CV Partners Overview</span><span class="desc">Strategy, Timeline, Principals, Process</span></li>
    <li><span class="num">07</span><span class="item">Appendix</span><span class="desc">Representative Transactions</span></li>
  </ol>
  <p class="foot">Calder Voss 2020 Confidential</p><p class="page">CALDER VOSS | 3</p>
</section>

<!-- Row 2 -->
<section class="slide c1 r2">
  <div class="dot-field" style="right:0;top:0;width:75px;height:35px"></div>
  <div class="dot-field" style="left:0;top:65px;width:22px;height:75px"></div>
  <h2 class="heading" style="top:11px;text-transform:none;font-size:8.5px">Agenda</h2>
  <p class="kicker" style="top:22px">May 27, 2021</p>
  <ol class="agenda" style="left:55px;top:28px;width:80px">
    <li><span class="num">01</span><span class="item">Welcome Message</span><span class="desc">Curabitur fermentum, arcuac</span></li>
    <li><span class="num">02</span><span class="item">Our Advisory Services</span><span class="desc">Curabitur fermentum, arcuac</span></li>
    <li><span class="num">03</span><span class="item">Market Overview</span><span class="desc">Submarket Overview &amp; Comparables</span></li>
    <li><span class="num">04</span><span class="item">Business Plan</span><span class="desc">Renovations, Timeline, Case Study</span></li>
    <li><span class="num">05</span><span class="item">Investment Structure</span><span class="desc">Summary of Terms, Sample Investment</span></li>
    <li><span class="num">06</span><span class="item">CV Partners</span><span class="desc">Strategy, Timeline, Principals, Process</span></li>
    <li><span class="num">07</span><span class="item">Case of Study</span><span class="desc">Representative Transactions</span></li>
  </ol>
  <ol class="agenda" start="8" style="left:137px;top:28px;width:90px">
    <li><span class="num">08</span><span class="item">Case of Study</span><span class="desc">Investment Highlights</span></li>
    <li><span class="num">09</span><span class="item">Property Overview</span><span class="desc">Property Description, Market Overview</span></li>
    <li><span class="num">10</span><span class="item">Market Overview</span><span class="desc">Submarket Overview &amp; Comparables</span></li>
    <li><span class="num">11</span><span class="item">Business Plan</span><span class="desc">Renovations, Timeline, Case Study</span></li>
    <li><span class="num">12</span><span class="item">Investment Structure</span><span class="desc">Summary of Terms, Sample Investment</span></li>
    <li><span class="num">13</span><span class="item">Case of Study</span><span class="desc">Strategy, Timeline, Principals, Process</span></li>
    <li><span class="num">14</span><span class="item" style="text-transform:none">Appendix</span><span class="desc">Representative Transactions</span></li>
  </ol>
  <p class="foot">Calder Voss 2020 Confidential</p><p class="page">CALDER VOSS | 4</p>
</section>

<section class="slide c2 r2">
  <h2 class="welcome" style="left:49px;top:22px">Welcome<br>Message</h2>
  <p class="body-copy" style="left:20px;top:53px;width:86px">Curabitur fermentum, arcu ac aliquam venenatis, sem massa lacinia dolor, vitae condimentum ante ligula vitae nunc lorem ipsum. Curabitur fermentum, arcu ac aliquam venenatis, sem massa lacinia dolor, vitae condimentum ante ligula vitae nunc lorem ipsum. Curabitur fermentum, arcu ac aliquam venenatis, sem massa lacinia dolor, vitae condimentum ante ligula vitae nunc lorem ipsum.</p>
  <p class="signed" style="left:60px;top:110px;width:46px">Peter Hale<small>Chairman Emeritus</small></p>
  <div class="photo" role="img" aria-label="Night view of glass office towers" style="left:124px;top:20px;width:110px;height:99px"></div>
  <p class="foot">Calder Voss 2020 Confidential</p><p class="page">CALDER VOSS | 5</p>
</section>

<section class="slide c3 r2">
  <div role="img" aria-label="Glass office tower seen from below against blue sky" style="left:0;top:0;width:95px;height:140px;background:linear-gradient(150deg,#9fc3df,#5c7f9e 55%,#6e8a5c)"></div>
  <div class="portrait" role="img" aria-label="Portrait of the chief executive" style="left:73px;top:47px;width:44px;height:44px"></div>
  <h2 class="welcome" style="left:154px;top:27px">Welcome<br>Message</h2>
  <p class="body-copy" style="left:129px;top:59px;width:105px">Curabitur fermentum, arcu ac aliquam venenatis, sem massa lacinia dolor, vitae condimentum ante ligula vitae nunc lorem ipsum. Curabitur fermentum, arcu ac aliquam venenatis, sem massa lacinia dolor, vitae condimentum ante ligula vitae nunc lorem ipsum. Curabitur fermentum, arcu ac aliquam venenatis, sem massa lacinia dolor, vitae condimentum ante ligula.</p>
  <p class="signed" style="left:180px;top:113px;width:55px">Marco Bellini<small>CEO</small></p>
  <p class="foot" style="left:100px">Calder Voss 2020 Confidential</p><p class="page">CALDER VOSS | 6</p>
</section>

<!-- Row 3 -->
<section class="slide c1 r3">
  <div class="portrait" role="img" aria-label="Portrait of the presenter" style="left:37px;top:31px;width:44px;height:44px;border:0"></div>
  <p style="left:20px;top:81px;width:78px;text-align:center;font-size:3px;line-height:1.4">Henry Marsh<br><span style="font-size:2.4px;color:var(--grey)">Executive Vice Chairman</span></p>
  <div style="left:54px;top:93px;width:4px;height:4px;background:var(--teal)"></div>
  <div style="left:59px;top:93px;width:4px;height:4px;background:var(--red)"></div>
  <div style="left:105px;top:41px;width:1px;height:52px;background:var(--line)"></div>
  <h2 class="heading" style="left:123px;top:48px;font-size:7.5px">Today Presenter</h2>
  <p class="body-copy" style="left:105px;top:64px;width:105px">Curabitur fermentum, arcu ac aliquam venenatis, sem massa lacinia dolor, vitae condimentum ante ligula vitae nunc lorem ipsum. Curabitur fermentum, arcu ac aliquam venenatis, sem massa lacinia dolor, vitae condimentum ante ligula vitae nunc lorem ipsum. Curabitur fermentum, arcu ac aliquam venenatis, sem massa lacinia dolor, vitae condi</p>
  <p style="left:180px;top:93px;font-size:2.6px;color:var(--grey)">Best Regards</p>
  <p class="foot">Calder Voss 2020 Confidential</p><p class="page">CALDER VOSS | 7</p>
</section>

<section class="slide c2 r3">
  <h2 class="heading">Our Advisory Services</h2>
  <p class="kicker" style="width:210px">Calder Voss has assembled a comprehensive set of integrated services that cover every aspect of corporate governance, shareholder communication and engagement. Our combination of local expertise and global perspective helps companies in different markets anticipate and respond appropriately to issues that are of concern to investors in their capacity as fiduciaries and long-term owners.</p>
  <div class="svc" style="left:30px;top:40px"></div><p class="svc-label" style="left:48px;top:41px">Corporate governance advisory services</p>
  <div class="svc" style="left:100px;top:40px"></div><p class="svc-label" style="left:118px;top:42px">ESG advisory services</p>
  <div class="svc" style="left:164px;top:40px"></div><p class="svc-label" style="left:182px;top:41px;width:40px">Proxy contests, hostile takeovers, shareholder activism and special situations</p>
  <div class="svc" style="left:30px;top:62px"></div><p class="svc-label" style="left:48px;top:64px">ESG survey services ESG monitoring</p>
  <div class="svc" style="left:100px;top:62px"></div><p class="svc-label" style="left:118px;top:64px">Capital market intelligence services</p>
  <div class="svc" style="left:164px;top:62px"></div><p class="svc-label" style="left:182px;top:64px;width:40px">Proxy solicitation and shareholder meeting services</p>
  <div class="svc" style="left:30px;top:84px"></div><p class="svc-label" style="left:48px;top:86px">Retail services and additional capabilities</p>
  <div class="svc" style="left:100px;top:84px"></div><p class="svc-label" style="left:118px;top:86px">Board of director services</p>
  <div class="svc" style="left:164px;top:84px"></div><p class="svc-label" style="left:182px;top:85px;width:42px">Services for registered funds – mutual funds, exchange traded funds and closed-end funds</p>
  <div class="svc" style="left:64px;top:106px"></div><p class="svc-label" style="left:82px;top:109px">SPAC advisory services</p>
  <div class="svc" style="left:136px;top:106px"></div><p class="svc-label" style="left:154px;top:111px">Debt services</p>
  <p class="foot">Calder Voss 2020 Confidential</p><p class="page">CALDER VOSS | 8</p>
</section>

<section class="slide c3 r3">
  <div class="dot-field" style="right:0;top:0;width:75px;height:35px"></div>
  <h2 class="heading">Our Advisory Services</h2>
  <p class="kicker" style="font-size:6.3px;top:22px">Retail Services and Additional Capabilities</p>
  <div class="tile-icon" style="left:11px;top:50px;width:48px;height:48px">
    <svg width="48" height="48" viewBox="0 0 48 48" fill="none" stroke="#fff" stroke-width="1.2"><circle cx="24" cy="16" r="4"/><circle cx="15" cy="22" r="3"/><circle cx="33" cy="22" r="3"/><path d="M17 36v-7a7 7 0 0114 0v7z"/><path d="M10 36v-5a5 5 0 019 0M38 36v-5a5 5 0 00-9 0"/></svg>
  </div>
  <ul class="bullets" style="left:70px;top:54px;width:170px">
    <li>Strategic advice on corporate governance, board issues, compensation, sustainability and shareholder activism</li>
    <li>Ownership profile and analysis of shareholder expectations</li>
    <li>Comprehensive review and preparation for the annual meeting</li>
    <li>Vote projections and updates on shareholder voting policies</li>
    <li>Document review and recommendations</li>
    <li>Outreach and engagement with key investors and proxy advisory firms</li>
    <li>Presentations to the board and management on relevant trends in governance, sustainability, shareholder rights and activism</li>
  </ul>
  <p class="foot">Calder Voss 2020 Confidential</p><p class="page">CALDER VOSS | 9</p>
</section>

<!-- Row 4 -->
<section class="slide c1 r4">
  <div class="dot-field" style="right:0;top:0;width:75px;height:35px"></div>
  <h2 class="heading">Our Advisory Services</h2>
  <p class="kicker" style="font-size:6.3px;top:22px">Retail Services and Additional Capabilities</p>
  <div class="tile-icon" style="left:11px;top:55px;width:48px;height:48px">
    <svg width="48" height="48" viewBox="0 0 48 48" fill="none" stroke="#fff" stroke-width="1.2"><circle cx="24" cy="21" r="7"/><path d="M15 22a9 9 0 0118 0M14 34c2-5 6-7 10-7s8 2 10 7z"/><path d="M33 22v3h-5"/></svg>
  </div>
  <ul class="bullets" style="left:105px;top:58px;width:130px;font-size:3.8px">
    <li>IPO Services</li>
    <li>Telephone solicitation campaigns</li>
    <li>Retail shareholder outreach programs</li>
    <li>Post-merger clean-up and asset reunification programs</li>
    <li>Odd-lot buyback situations</li>
    <li>Vote tabulation services</li>
    <li>Inspector of Election services</li>
    <li>Expert witness testimony services</li>
  </ul>
  <p class="foot">Calder Voss 2020 Confidential</p><p class="page">CALDER VOSS | 10</p>
</section>

<section class="slide c2 r4">
  <div class="photo" role="img" aria-label="City skyline of office towers at dusk" style="left:0;top:0;width:247px;height:70px"></div>
  <h2 class="heading center" style="top:29px;color:#fff;font-size:9.5px;font-weight:300">Company Insights</h2>
  <p class="col-num" style="left:13px;top:85px">01</p>
  <p class="col-head" style="left:36px;top:87px">Lorem ipsum dolor</p>
  <p class="col-copy" style="left:36px;top:92px">Curabitur fermentum, arcu ac aliquam venenatis, sem massa lacinia dolor, vitae condimentum ante ligula vitae nunc lorem ipsum.</p>
  <p class="col-num" style="left:90px;top:85px">02</p>
  <p class="col-head" style="left:113px;top:87px">Lorem ipsum dolor</p>
  <p class="col-copy" style="left:113px;top:92px">Curabitur fermentum, arcu ac aliquam venenatis, sem massa lacinia dolor, vitae condimentum ante ligula vitae nunc lorem ipsum.</p>
  <p class="col-num" style="left:167px;top:85px">03</p>
  <p class="col-head" style="left:190px;top:87px">Lorem ipsum dolor</p>
  <p class="col-copy" style="left:190px;top:92px">Curabitur fermentum, arcu ac aliquam venenatis, sem massa lacinia dolor, vitae condimentum ante ligula vitae nunc lorem ipsum.</p>
  <p class="foot">Calder Voss 2020 Confidential</p><p class="page">CALDER VOSS | 11</p>
</section>

<section class="slide c3 r4">
  <div class="dot-field" style="right:0;top:0;width:75px;height:35px"></div>
  <div class="dot-field" style="left:0;top:62px;width:22px;height:78px"></div>
  <h2 class="heading">Company Insights</h2>
  <p class="kicker" style="width:110px">Curabitur fermentum, arcu ac aliquam venenatis, sem massa lacinia dolor, vitae condimentum ante ligula vitae nunc lorem ipsum.</p>
  <p class="big-num" style="left:33px;top:48px">267</p><p class="num-label" style="left:31px;top:67px">Lorem ipsum dolor</p>
  <p class="big-num" style="left:81px;top:48px">1023</p><p class="num-label" style="left:84px;top:67px">Lorem ipsum dolor</p>
  <p class="big-num" style="left:141px;top:81px">34</p><p class="num-label" style="left:135px;top:100px">Lorem ipsum dolor</p>
  <p class="big-num" style="left:180px;top:81px">121</p><p class="num-label" style="left:179px;top:100px">Lorem ipsum dolor</p>
  <p class="foot">Calder Voss 2020 Confidential</p><p class="page">CALDER VOSS | 12</p>
</section>

<!-- Row 5 -->
<section class="slide c1 r5">
  <h2 class="heading center">Company Insights</h2>
  <p class="kicker center" style="left:60px;width:127px">Curabitur fermentum, arcu ac aliquam venenatis, sem massa lacinia dolor, vitae condimentum ante ligula vitae nunc lorem ipsum.</p>
  <svg style="left:0;top:0" width="247" height="140" viewBox="0 0 247 140">
    <circle cx="123" cy="81" r="16" fill="#000"/>
    <text x="123" y="80" font-size="2.6" fill="#fff" text-anchor="middle" letter-spacing="1.2">CALDER</text>
    <text x="123" y="84" font-size="2.6" fill="#fff" text-anchor="middle" letter-spacing="1.2">VOSS</text>
    <circle cx="96" cy="54" r="11" fill="var(--teal)"/>
    <circle cx="148" cy="54" r="11" fill="var(--navy)"/>
    <circle cx="96" cy="108" r="11" fill="var(--blue)"/>
    <circle cx="148" cy="108" r="11" fill="var(--charcoal)"/>
    <g fill="none" stroke="#fff" stroke-width=".7">
      <rect x="91" y="49" width="10" height="10"/><path d="M91 54h10M96 49v10"/>
      <circle cx="148" cy="54" r="5"/><path d="M143 54h10M148 49c-3 3-3 7 0 10c3-3 3-7 0-10"/>
      <path d="M96 102v11M90 105h12M90 105l-2 4h4zM102 105l-2 4h4z"/>
      <path d="M142 108l4-3 3 2 5-3M143 110l4 3 6-4"/>
    </g>
    <g font-size="2.6" fill="var(--teal)"><text x="38" y="50">LOREM IPSUM DOLOR</text><text x="38" y="99">LOREM IPSUM DOLOR</text><text x="221" y="50" text-anchor="end">LOREM IPSUM DOLOR</text><text x="218" y="99" text-anchor="end">LOREM IPSUM DOLOR</text></g>
    <g font-size="8" font-weight="300" fill="var(--navy)"><text x="29" y="53">1</text><text x="29" y="102">2</text><text x="222" y="53">3</text><text x="222" y="102">4</text></g>
  </svg>
  <p class="col-copy" style="left:20px;top:55px;width:55px">Curabitur fermentum, arcu ac aliquam venenatis, sem massa lacinia dolor, vitae condimentum ante ligula vitae nunc lorem ipsum.</p>
  <p class="col-copy" style="left:20px;top:104px;width:55px">Curabitur fermentum, arcu ac aliquam venenatis, sem massa lacinia dolor, vitae condimentum ante ligula vitae nunc lorem ipsum.</p>
  <p class="col-copy" style="left:172px;top:55px;width:55px;text-align:right">Curabitur fermentum, arcu ac aliquam venenatis, sem massa lacinia dolor, vitae condimentum ante ligula vitae nunc lorem ipsum.</p>
  <p class="col-copy" style="left:172px;top:104px;width:55px;text-align:right">Curabitur fermentum, arcu ac aliquam venenatis, sem massa lacinia dolor, vitae condimentum ante ligula vitae nunc lorem ipsum.</p>
  <p class="foot">Calder Voss 2020 Confidential</p><p class="page">CALDER VOSS | 13</p>
</section>

<section class="slide c2 r5">
  <h2 class="heading center">Company Insights</h2>
  <p class="kicker center">Curabitur fermentum, arcu ac aliquam venenatis, sem massa lacinia dolor, vitae condimentum ante ligula vitae nunc lorem ipsum.</p>
  <svg style="left:0;top:0" width="247" height="140" viewBox="0 0 247 140">
    <g fill="none" stroke-width="1">
      <circle cx="40" cy="66" r="22" stroke="#e6e6e6"/>
      <circle cx="40" cy="66" r="22" stroke="var(--teal)" stroke-dasharray="109 138" transform="rotate(-90 40 66)"/>
      <circle cx="96" cy="66" r="22" stroke="#e6e6e6"/>
      <circle cx="96" cy="66" r="22" stroke="var(--red)" stroke-dasharray="134 138" transform="rotate(-90 96 66)"/>
      <circle cx="151" cy="66" r="22" stroke="#e6e6e6"/>
      <circle cx="151" cy="66" r="22" stroke="var(--blue)" stroke-dasharray="73 138" transform="rotate(-90 151 66)"/>
      <circle cx="207" cy="66" r="22" stroke="#e6e6e6"/>
      <circle cx="207" cy="66" r="22" stroke="var(--charcoal)" stroke-dasharray="98 138" transform="rotate(-90 207 66)"/>
    </g>
    <g font-size="12" font-weight="300" text-anchor="middle">
      <text x="40" y="70" fill="var(--teal)">79%</text><text x="96" y="70" fill="var(--red)">97%</text>
      <text x="151" y="70" fill="var(--blue)">53%</text><text x="207" y="70" fill="var(--charcoal)">71%</text>
    </g>
    <g font-size="2.6" text-anchor="middle" fill="#444">
      <text x="40" y="95">LOREM IPSUM DOLOR</text><text x="96" y="95">LOREM IPSUM DOLOR</text><text x="151" y="95">LOREM IPSUM DOLOR</text><text x="207" y="95">LOREM IPSUM DOLOR</text>
    </g>
    <g font-size="2.4" text-anchor="middle" fill="var(--teal)">
      <text x="40" y="100">Curabitur fermentum, arcu ac</text><text x="40" y="103">aliquam venenatis, sem</text><text x="40" y="106">massa lacinia dolor, vitae</text><text x="40" y="109">condimentum ante ligula</text>
      <text x="96" y="100">Curabitur fermentum, arcu ac</text><text x="96" y="103">aliquam venenatis, sem</text><text x="96" y="106">massa lacinia dolor, vitae</text><text x="96" y="109">condimentum ante ligula</text>
      <text x="151" y="100">Curabitur fermentum, arcu ac</text><text x="151" y="103">aliquam venenatis, sem</text><text x="151" y="106">massa lacinia dolor, vitae</text><text x="151" y="109">condimentum ante ligula</text>
      <text x="207" y="100">Curabitur fermentum, arcu ac</text><text x="207" y="103">aliquam venenatis, sem</text><text x="207" y="106">massa lacinia dolor, vitae</text><text x="207" y="109">condimentum ante ligula</text>
    </g>
  </svg>
  <p class="foot">Calder Voss 2020 Confidential</p><p class="page">CALDER VOSS | 14</p>
</section>

<section class="slide c3 r5">
  <h2 class="heading center">Company Insights</h2>
  <p class="kicker center">Curabitur fermentum, arcu ac aliquam venenatis, sem massa lacinia dolor, vitae condimentum ante ligula vitae nunc lorem ipsum.</p>
  <div class="tile" style="left:19px;top:37px;width:80px;height:40px;background:var(--teal-soft);padding-left:24px"><b>Lorem ipsum dolor sit amet</b><span>Curabitur fermentum, arcu ac aliquam venenatis, sem massa lacinia dolor, vitae condimentum ante ligula vitae nunc lorem</span></div>
  <div class="tile" style="left:19px;top:79px;width:80px;height:41px;background:var(--teal-soft);padding-left:24px"><b>Lorem ipsum dolor sit amet</b><span>Curabitur fermentum, arcu ac aliquam venenatis, sem massa lacinia dolor, vitae condimentum ante ligula vitae nunc lorem</span></div>
  <div class="tile" style="left:101px;top:37px;width:46px;height:83px;background:var(--teal-dark);padding-top:24px"><b>Lorem ipsum dolor sit amet</b><span>Curabitur at fermentum, arcu ac sit aliquam venenatis, sem massa lacinia at dolor, vitae condimentum luck ante ligula vitae nunc lorem ipsum.</span></div>
  <div class="tile" style="left:149px;top:37px;width:80px;height:40px;background:var(--blue);padding-left:24px"><b>Lorem ipsum dolor sit amet</b><span>Curabitur fermentum, arcu ac aliquam venenatis, sem massa lacinia dolor, vitae condimentum ante ligula vitae nunc lorem</span></div>
  <div class="tile" style="left:149px;top:79px;width:80px;height:41px;background:var(--charcoal);padding-left:24px"><b>Lorem ipsum dolor sit amet</b><span>Curabitur fermentum, arcu ac aliquam venenatis, sem massa lacinia dolor, vitae condimentum ante ligula vitae nunc lorem</span></div>
  <p class="foot">Calder Voss 2020 Confidential</p><p class="page">CALDER VOSS | 15</p>
</section>

<!-- Row 6 -->
<section class="slide c1 r6">
  <div class="dot-field" style="right:0;top:0;width:75px;height:35px"></div>
  <h2 class="heading">Composition of Resources</h2>
  <p class="kicker" style="width:110px">Curabitur fermentum, arcu ac aliquam venenatis, sem massa lacinia dolor, vitae condimentum ante ligula vitae nunc lorem ipsum.</p>
  <p style="left:37px;top:60px;width:42px;font-size:4.2px;line-height:1.3;color:var(--teal-soft);font-weight:300">Curabitur set at noun fermentum, arcu ac aliquam venenatis, sem massa lacinia dolor, vitae toes condimentum ante ligula set noun</p>
  <svg style="left:0;top:0" width="247" height="140" viewBox="0 0 247 140">
    <path d="M133 26a17 17 0 0117 17c0 9-9 15-17 25c-8-10-17-16-17-25a17 17 0 0117-17z" fill="var(--teal)"/>
    <circle cx="133" cy="42" r="13" fill="#fff"/>
    <path d="M180 50a23 23 0 110 46c-11 0-20-8-34-23c14-15 23-23 34-23z" fill="var(--red)"/>
    <circle cx="180" cy="73" r="18" fill="#fff"/>
    <path d="M133 121a17 17 0 01-17-17c0-9 9-15 17-25c8 10 17 16 17 25a17 17 0 01-17 17z" fill="var(--navy)"/>
    <circle cx="133" cy="104" r="13" fill="#fff"/>
    <path d="M106 61a12 12 0 100 24c6 0 10-5 20-12c-10-7-14-12-20-12z" fill="var(--teal-soft)"/>
    <circle cx="106" cy="73" r="9" fill="#fff"/>
    <g font-weight="300" text-anchor="middle" fill="#333">
      <text x="133" y="43" font-size="7">30<tspan font-size="3">%</tspan></text>
      <text x="180" y="73" font-size="7">45<tspan font-size="3">%</tspan></text>
      <text x="106" y="75" font-size="6">10<tspan font-size="3">%</tspan></text>
      <text x="133" y="105" font-size="7">15<tspan font-size="3">%</tspan></text>
    </g>
    <g font-size="2.3" text-anchor="middle" fill="#555">
      <text x="133" y="47">Book and article</text><text x="133" y="50">summaries</text>
      <text x="180" y="78">Presentations &amp;</text><text x="180" y="81">related assets</text>
      <text x="106" y="79">Interviews</text>
      <text x="133" y="109">Exclusive</text><text x="133" y="112">insights</text>
    </g>
  </svg>
  <p class="foot">Calder Voss 2020 Confidential</p><p class="page">CALDER VOSS | 16</p>
</section>

<section class="slide c2 r6">
  <h2 class="heading">Strategic Roadmap - Swimlane View</h2>
  <svg style="left:0;top:0" width="247" height="140" viewBox="0 0 247 140">
    <rect x="34" y="29" width="45" height="5" fill="var(--teal-soft)"/><rect x="80" y="29" width="45" height="5" fill="var(--navy)"/>
    <rect x="126" y="29" width="45" height="5" fill="var(--blue)"/><rect x="172" y="29" width="45" height="5" fill="var(--red)"/>
    <g font-size="2.2" fill="#fff" text-anchor="middle" letter-spacing=".6"><text x="56" y="32.5">PRODUCT</text><text x="102" y="32.5">FINANCE</text><text x="148" y="32.5">SALES</text><text x="194" y="32.5">MARKETING</text></g>
    <g fill="none" stroke="var(--navy)" stroke-width=".6"><rect x="24" y="36" width="194" height="26"/><rect x="24" y="64" width="194" height="20"/><rect x="24" y="86" width="194" height="35"/></g>
    <g font-size="2" fill="var(--navy)"><text transform="translate(28 54) rotate(-90)">PROPOSED</text><text transform="translate(28 80) rotate(-90)">IN PROGRESS</text><text transform="translate(28 110) rotate(-90)">SCHEDULED</text></g>
    <g fill="#fff" stroke="#ccc" stroke-width=".3">
      <rect x="36" y="38" width="40" height="4"/><rect x="36" y="44" width="40" height="4"/><rect x="36" y="50" width="40" height="4"/><rect x="36" y="56" width="40" height="4"/>
      <rect x="82" y="38" width="40" height="4"/><rect x="82" y="44" width="40" height="4"/><rect x="82" y="50" width="40" height="4"/>
      <rect x="128" y="38" width="40" height="4"/><rect x="128" y="44" width="40" height="4"/><rect x="128" y="50" width="40" height="4"/><rect x="128" y="56" width="40" height="4"/>
      <rect x="174" y="38" width="40" height="4"/><rect x="174" y="44" width="40" height="4"/>
      <rect x="36" y="66" width="40" height="4"/><rect x="36" y="72" width="40" height="4"/><rect x="36" y="78" width="40" height="4"/>
      <rect x="82" y="66" width="40" height="4"/><rect x="82" y="72" width="40" height="4"/>
      <rect x="128" y="66" width="40" height="4"/><rect x="128" y="72" width="40" height="4"/>
      <rect x="174" y="66" width="40" height="4"/><rect x="174" y="72" width="40" height="4"/><rect x="174" y="78" width="40" height="4"/>
      <rect x="36" y="88" width="40" height="4"/><rect x="36" y="94" width="40" height="4"/><rect x="36" y="100" width="40" height="4"/><rect x="36" y="106" width="40" height="4"/><rect x="36" y="112" width="40" height="4"/>
      <rect x="82" y="88" width="40" height="4"/>
      <rect x="128" y="88" width="40" height="4"/><rect x="128" y="94" width="40" height="4"/>
      <rect x="174" y="88" width="40" height="4"/><rect x="174" y="94" width="40" height="4"/><rect x="174" y="100" width="40" height="4"/><rect x="174" y="106" width="40" height="4"/>
    </g>
    <g font-size="1.7" fill="#555">
      <text x="38" y="40.7">API web services</text><text x="38" y="46.7">SSL support</text><text x="38" y="52.7">Identify customer values</text><text x="38" y="58.7">CRM integration</text>
      <text x="84" y="40.7">Stream financial reporting</text><text x="84" y="46.7">Finalise 2021 budget</text><text x="84" y="52.7">Finalise 2022 budget</text>
      <text x="130" y="40.7">Engage key vendors</text><text x="130" y="46.7">Profit opportunities</text><text x="130" y="52.7">Negotiate 2021 deal</text><text x="130" y="58.7">Connect with distributor</text>
      <text x="176" y="40.7">Lead generation strategies</text><text x="176" y="46.7">Group discount plan</text>
      <text x="38" y="68.7">Live chat</text><text x="38" y="74.7">Push notification</text><text x="38" y="80.7">Analytics</text>
      <text x="84" y="68.7">Breakdown analysis</text><text x="84" y="74.7">Cost and complexity drivers</text>
      <text x="130" y="68.7">Launch roadshow</text><text x="130" y="74.7">Competitor review</text>
      <text x="176" y="68.7">Competitor analysis</text><text x="176" y="74.7">Influencer platform</text><text x="176" y="80.7">Launch monthly review</text>
      <text x="38" y="90.7">Sprint single sign on</text><text x="38" y="96.7">Stakeholder community</text><text x="38" y="102.7">Cloud support</text><text x="38" y="108.7">Improve service levels</text><text x="38" y="114.7">Account management</text>
      <text x="84" y="90.7">Streamline vendor management</text>
      <text x="130" y="90.7">Analyse sales trends</text><text x="130" y="96.7">Define sales territories</text>
      <text x="176" y="90.7">Partnerships</text><text x="176" y="96.7">Industry studies</text><text x="176" y="102.7">Schedule focus group</text><text x="176" y="108.7">Diversification</text>
    </g>
  </svg>
  <p class="foot">Calder Voss 2020 Confidential</p><p class="page">CALDER VOSS | 17</p>
</section>

<section class="slide c3 r6">
  <h2 class="heading">Strategic Roadmap</h2>
  <svg style="left:0;top:0" width="247" height="140" viewBox="0 0 247 140">
    <rect x="24" y="27" width="30" height="97" fill="#f1f1f1"/>
    <rect x="54" y="27" width="165" height="97" fill="#f7f7f7"/>
    <rect x="56" y="26" width="152" height="95" fill="none" stroke="var(--red)" stroke-width=".5"/>
    <g stroke="#ddd" stroke-width=".4"><path d="M24 33h195M24 48h195M24 63h195M24 113h195"/></g>
    <g font-size="2.5" font-weight="700" fill="#333" text-anchor="middle">
      <text x="39" y="31">MISSION</text><text x="39" y="42">VALUES</text><text x="39" y="55">INGREDIENTS</text><text x="39" y="58">FOR CHANGE</text><text x="39" y="89">BY YEAR 2</text><text x="39" y="118">BY YEAR 3</text>
    </g>
    <g font-size="1.8" fill="#444" text-anchor="middle">
      <text x="132" y="31">To connect, support and inform efforts to improve the health of individuals and communities in city based sources</text>
      <text x="74" y="38" font-weight="700">EMPATHY</text><text x="103" y="38" font-weight="700">EQUITY</text><text x="132" y="38" font-weight="700">INTEGRITY</text><text x="161" y="38" font-weight="700">OPENNESS</text><text x="190" y="38" font-weight="700">KNOWLEDGE</text>
      <text x="74" y="42">Feeling from another's</text><text x="103" y="42">Prioritising the most</text><text x="132" y="42">Transparency, honesty</text><text x="161" y="42">Listening, adapting and</text><text x="190" y="42">Embracing community</text>
      <text x="74" y="44.5">perspective</text><text x="103" y="44.5">impacted</text><text x="132" y="44.5">and accountability</text><text x="161" y="44.5">experimenting</text><text x="190" y="44.5">wisdom</text>
      <text x="74" y="55">Policy, systems &amp;</text><text x="74" y="57.5">environmental change</text><text x="103" y="56">Multi-sector partnerships</text><text x="132" y="56">Paradigm shift</text><text x="161" y="56">Community-driven solutions</text><text x="190" y="56">Build trust and equity</text>
      <text x="132" y="67">Company will identify and build relationships with stakeholders and develop strategies to support progression along the collaboration</text>
      <text x="132" y="69.5">continuum</text>
      <text x="132" y="118">Company will support stakeholders in building networks of collaborative health champions</text>
    </g>
    <rect x="62" y="73" width="140" height="32" fill="#fff" stroke="#ddd" stroke-width=".3"/>
    <g font-size="1.9" font-weight="700" fill="var(--navy)" text-anchor="middle"><text x="76" y="78">RESISTANT</text><text x="104" y="78">CURIOUS</text><text x="132" y="78">AWARE</text><text x="160" y="78">ADVOCATE</text><text x="188" y="78">CHAMPION</text></g>
    <g font-size="1.6" fill="#555">
      <text x="66" y="82">• Believes key job</text><text x="66" y="85">doesn't impact health</text><text x="66" y="88">• Prefers comfort zone</text>
      <text x="94" y="82">• Interested in what</text><text x="94" y="85">customers are up to</text><text x="94" y="88">• Gets connected to a</text><text x="94" y="91">trusted source</text>
      <text x="122" y="82">• Validates</text><text x="122" y="85">intersections</text><text x="122" y="88">• Expresses need</text><text x="122" y="91">• Energised</text>
      <text x="150" y="82">• Influences others</text><text x="150" y="85">• Practices buy-in</text><text x="150" y="88">• Drives real change</text><text x="150" y="91">at work</text>
      <text x="178" y="82">• Recruits new</text><text x="178" y="85">partners</text><text x="178" y="88">• Collaborates</text><text x="178" y="91">• Practice leads</text>
    </g>
  </svg>
  <p class="foot">Calder Voss 2020 Confidential</p><p class="page">CALDER VOSS | 18</p>
</section>

<!-- Row 7 -->
<section class="slide c1 r7">
  <h2 class="heading">Areas for Change</h2>
  <svg style="left:0;top:0" width="247" height="140" viewBox="0 0 247 140">
    <rect x="16" y="27" width="163" height="6" fill="#e9e9e9"/>
    <g font-size="2" font-weight="700" fill="#333"><text x="25" y="31">CHARACTERISTICS</text><text x="107" y="31">DESCRIBE THE CHANGE</text></g>
    <rect x="73" y="34" width="22" height="79" rx="2" fill="none" stroke="var(--navy)" stroke-width=".6"/>
    <g stroke="#e2e2e2" stroke-width=".3"><path d="M16 40h163M16 46h163M16 52h163M16 58h163M16 64h163M16 70h163M16 76h163M16 82h163M16 88h163M16 94h163M16 100h163M16 106h163"/></g>
    <g font-size="1.8" fill="#444">
      <text x="25" y="38">Brand identity</text><text x="25" y="44">Culture/behaviour of our team</text><text x="25" y="50">Our advice/practice philosophies</text><text x="25" y="56">Client/service value proposition</text><text x="25" y="62">Ideal client</text><text x="25" y="68">Fee model/revenue mix</text><text x="25" y="74">Scale of our practice</text><text x="25" y="80">Talent/skills/education of our team</text><text x="25" y="86">Locations</text><text x="25" y="92">Use of technology</text><text x="25" y="98">Communications &amp; marketing</text>
    </g>
    <g font-size="1.8" fill="var(--teal)"><text x="99" y="38">Write a text for describing changes</text><text x="99" y="44">Write a text for describing changes</text><text x="99" y="50">Write a text for describing changes</text><text x="99" y="56">Write a text for describing changes</text><text x="99" y="62">Write a text for describing changes</text><text x="99" y="68">Write a text for describing changes</text><text x="99" y="74">Write a text for describing changes</text><text x="99" y="80">Write a text for describing changes</text><text x="99" y="86">Write a text for describing changes</text><text x="99" y="92">Write a text for describing changes</text><text x="99" y="98">Write a text for describing changes</text></g>
    <g fill="none" stroke="var(--navy)" stroke-width=".6">
      <path d="M82 37l1.5 1.5 3-3"/><path d="M82 43l3 3M85 43l-3 3"/><path d="M82 49l3 3M85 49l-3 3"/><path d="M82 55l3 3M85 55l-3 3"/><path d="M82 61l3 3M85 61l-3 3"/>
      <path d="M82 67l3 3M85 67l-3 3"/><path d="M82 73l1.5 1.5 3-3"/><path d="M82 79l1.5 1.5 3-3"/><path d="M82 85l1.5 1.5 3-3"/><path d="M82 91l1.5 1.5 3-3"/><path d="M82 97l1.5 1.5 3-3"/>
    </g>
    <rect x="181" y="27" width="53" height="97" rx="2" fill="var(--navy)"/>
  </svg>
  <p style="left:185px;top:32px;width:46px;font-size:2.6px;line-height:1.35;color:#8fa3cf;font-weight:300">Lorem ipsum dolor sit amet, consectetur adipiscing elit, sed do eiusmod tempor incididunt ut labore et dolore magna aliqua. Ut enim ad minim veniam, quis nostrud exercitation ullamco laboris nisi ut aliquip ex ea commodo consequat. Duis aute irure dolor in reprehenderit in voluptate velit esse cillum dolore eu fugiat nulla pariatur. Excepteur sint occaecat cupidatat non proident, sunt in culpa qui officia deserunt mollit anim id est laborum.</p>
  <p class="foot">Calder Voss 2020 Confidential</p><p class="page">CALDER VOSS | 19</p>
</section>

<section class="slide c2 r7">
  <svg style="left:0;top:0" width="247" height="140" viewBox="0 0 247 140">
    <path d="M58 140a66 66 0 01132 0" fill="none" stroke="#e3e3e3" stroke-width="1"/>
    <path d="M66 140a58 58 0 01116 0" fill="none" stroke="var(--teal-soft)" stroke-width="1.3"/>
    <path d="M92 140a32 30 0 0164 0z" fill="#000"/>
    <g fill="var(--teal)"><circle cx="124" cy="82" r="1.5"/><circle cx="83" cy="99" r="1.5"/><circle cx="165" cy="99" r="1.5"/><circle cx="69" cy="123" r="1.5"/><circle cx="179" cy="123" r="1.5"/></g>
    <g fill="#efefef"><circle cx="124" cy="60" r="7"/><circle cx="72" cy="78" r="7"/><circle cx="176" cy="78" r="7"/><circle cx="39" cy="108" r="7"/><circle cx="209" cy="108" r="7"/></g>
    <g font-size="2" font-weight="700" fill="#333" text-anchor="middle"><text x="124" y="61">INDICATE</text><text x="72" y="79">TRANSLATE</text><text x="176" y="79">DEDICATE</text><text x="39" y="109">ILLUSTRATE</text><text x="209" y="109">OPERATE</text></g>
    <g font-size="1.8" fill="#555" text-anchor="middle">
      <text x="124" y="9">Develop the measurement</text><text x="124" y="12">systems &amp; data which illustrate</text><text x="124" y="15">the linkage between process</text><text x="124" y="18">behavior &amp; performance</text>
      <text x="72" y="26">Determine how, where and by how</text><text x="72" y="29">much business process can</text><text x="72" y="32">influence the strategic and/or</text><text x="72" y="35">process objectives</text>
      <text x="176" y="26">Identify &amp; engage the right people with</text><text x="176" y="29">the right reporting system, disciplines &amp;</text><text x="176" y="32">accountability to evaluate or improve</text><text x="176" y="35">process</text>
      <text x="39" y="73">Develop the right process maps</text><text x="39" y="76">which accurately reflect how value</text><text x="39" y="79">is created for customers through</text><text x="39" y="82">business processes</text>
      <text x="209" y="73">Fully integrate process based</text><text x="209" y="76">reporting disciplines and tools into</text><text x="209" y="79">process management action</text><text x="209" y="82">planning &amp; performance</text>
    </g>
    <g font-size="5" font-weight="700" fill="#fff" text-anchor="middle" letter-spacing=".5"><text x="124" y="124">ROADMAP</text><text x="124" y="132">DEVELOPMENT</text></g>
  </svg>
  <p class="foot">Calder Voss 2020 Confidential</p><p class="page">CALDER VOSS | 20</p>
</section>

<section class="slide c3 r7">
  <h2 class="heading">Strategy Map</h2>
  <p class="kicker">Curabitur fermentum, arcu ac aliquam venenatis, sem massa lacinia dolor, vitae condimentum ante ligula vitae nunc lorem ipsum.</p>
  <svg style="left:0;top:0" width="247" height="140" viewBox="0 0 247 140">
    <rect x="23" y="30" width="201" height="22" fill="#eef3f2"/>
    <rect x="23" y="54" width="201" height="17" fill="#eef3f2"/>
    <rect x="23" y="73" width="201" height="21" fill="#eef3f2"/>
    <rect x="23" y="96" width="201" height="23" fill="#eef3f2"/>
    <g fill="none" stroke="var(--teal)" stroke-width=".4"><path d="M130 35c-25 0-45 5-50 10M130 35c25 0 45 5 52 10M130 35v10M130 35c40 0 60 5 72 10"/></g>
    <g fill="var(--teal)"><rect x="113" y="31" width="30" height="5" rx="2.5"/><rect x="62" y="44" width="30" height="4" rx="2"/><rect x="99" y="44" width="30" height="4" rx="2"/><rect x="136" y="44" width="30" height="4" rx="2"/><rect x="173" y="44" width="30" height="4" rx="2"/></g>
    <g fill="var(--blue)"><rect x="62" y="60" width="16" height="4" rx="2"/><rect x="81" y="60" width="16" height="4" rx="2"/><rect x="100" y="60" width="16" height="4" rx="2"/><rect x="119" y="60" width="16" height="4" rx="2"/><rect x="138" y="60" width="16" height="4" rx="2"/><rect x="157" y="60" width="16" height="4" rx="2"/><rect x="176" y="60" width="16" height="4" rx="2"/><rect x="195" y="60" width="16" height="4" rx="2"/></g>
    <g fill="var(--charcoal)"><rect x="62" y="76" width="34" height="4" rx="1"/><rect x="100" y="76" width="34" height="4" rx="1"/><rect x="138" y="76" width="34" height="4" rx="1"/><rect x="176" y="76" width="34" height="4" rx="1"/></g>
    <g fill="var(--red)"><rect x="62" y="101" width="34" height="12" rx="1"/><rect x="100" y="101" width="34" height="12" rx="1"/><rect x="138" y="101" width="34" height="12" rx="1"/><rect x="176" y="101" width="34" height="12" rx="1"/></g>
    <g font-size="1.9" fill="#fff" text-anchor="middle">
      <text x="128" y="34.3">Long term</text>
      <text x="77" y="46.8">Improve cost structure</text><text x="114" y="46.8">Increase asset utilisation</text><text x="151" y="46.8">Expand revenue</text><text x="188" y="46.8">Enhance customer value</text>
      <text x="70" y="62.8">Price</text><text x="89" y="62.8">Quality</text><text x="108" y="62.8">Availability</text><text x="127" y="62.8">Selection</text><text x="146" y="62.8">Function</text><text x="165" y="62.8">Service</text><text x="184" y="62.8">Partnership</text><text x="203" y="62.8">Brand</text>
      <text x="79" y="78.8">Operations processes</text><text x="117" y="78.8">Customer processes</text><text x="155" y="78.8">Innovation processes</text><text x="193" y="78.8">Regulatory processes</text>
      <text x="79" y="106">Active participation</text><text x="79" y="109">among everyone</text><text x="117" y="106">Quality, sufficient and</text><text x="117" y="109">attractive workplace</text><text x="155" y="106">Right competence and</text><text x="155" y="109">correct skill analysis</text><text x="193" y="106">High availability of</text><text x="193" y="109">information support</text>
    </g>
    <g font-size="1.7" fill="#444" text-anchor="middle">
      <text x="136" y="57.5">CUSTOMER VALUE PROPOSITION</text><text x="108" y="68">Product/Service Attribute</text><text x="165" y="68">Relationship</text><text x="203" y="68">Image</text>
      <text x="79" y="84">Supply production</text><text x="79" y="86.5">management</text><text x="117" y="84">Selection acquisition</text><text x="117" y="86.5">retention growth</text><text x="155" y="84">Opportunity identification</text><text x="155" y="86.5">design development</text><text x="193" y="84">Environment safety</text><text x="193" y="86.5">and community</text>
    </g>
    <g font-size="2.4" font-weight="700" fill="#333" text-anchor="middle"><text x="38" y="48">FINANCIAL</text><text x="38" y="67">CUSTOMER</text><text x="38" y="88">INTERNAL</text><text x="38" y="111">LEARNING</text><text x="38" y="114">&amp; GROWTH</text></g>
    <g fill="none" stroke="var(--navy)" stroke-width=".5"><rect x="35" y="38" width="6" height="4"/><circle cx="38" cy="61" r="2"/><path d="M35 66a3 3 0 016 0"/><rect x="35" y="81" width="6" height="3" rx="1"/><path d="M35 108l2-3 2 1 2-3"/></g>
  </svg>
  <p class="foot">Calder Voss 2020 Confidential</p><p class="page">CALDER VOSS | 21</p>
</section>

</main>
</body>
</html>
```